Craft Brewery needs a banner design for a festival

We need a Large banner design for the Harvest at Bellmoor festival.We would like to see a lot of natural rainforest theme with small creeks and rivers as our name is Grey Owl Brewing co.

We need this to look attractive to our brand of naturally brewed beers.

Banner dimension are
3000mm Width
1150mm Height

Hey guys thanks for the designs, i have added a couple of more pics for inspiration one with ferns which we would like in the design and the other named tralvick which i like the background with all the brewing pics. Cheers Dale

Target Market(s)

Beer drinkers

Colors

Designer to choose colors to be used in the design.

Requirements
Must have
• Rainforest, Streams and rivers, nature, Logo
• The ingredients
Nice to have
• na
Should not have
• Na

```html
<!DOCTYPE html>
<html lang="en">
<head>
<meta charset="utf-8">
<title>Grey Owl Brewing Co – Harvest at Bellmoor Banner</title>
<link rel="stylesheet" href="https://fonts.googleapis.com/css2?family=Kaushan+Script&family=Oswald:wght@400&display=swap">
<style>
  :root {
    --forest-deep: #141a0c;
    --forest-dark: #24301a;
    --pine-green: #3d4d24;
    --autumn-gold: #d2a02a;
    --autumn-amber: #b3741c;
    --leaf-red: #c9481c;
    --leaf-orange: #d8761f;
    --sky-pale: #e6e7e4;
    --water-dark: #17140d;
    --water-brown: #4a3414;
    --bank-ochre: #8a6a3a;
    --rock-grey: #8c8272;
    --text-light: #ffffff;
  }
  * { margin: 0; padding: 0; box-sizing: border-box; }
  html, body {
    width: 1200px;
    height: 460px;
    overflow: hidden;
    background: var(--forest-deep);
  }
  .banner {
    position: relative;
    width: 1200px;
    height: 460px;
    overflow: hidden;
  }
  .banner__scene {
    position: absolute;
    inset: 0;
    background:
      /* overcast sky between the tree lines */
      radial-gradient(ellipse 230px 95px at 540px 10px, var(--sky-pale) 0%, rgba(230,231,228,0.85) 50%, rgba(230,231,228,0) 100%),
      /* still creek water */
      radial-gradient(ellipse 300px 90px at 600px 400px, var(--water-dark) 0%, rgba(23,20,13,0.9) 55%, rgba(23,20,13,0) 100%),
      radial-gradient(ellipse 200px 60px at 560px 345px, rgba(74,52,20,0.9) 0%, rgba(74,52,20,0) 100%),
      /* rocky bank */
      radial-gradient(ellipse 130px 40px at 540px 300px, rgba(140,130,114,0.8) 0%, rgba(140,130,114,0) 100%),
      radial-gradient(ellipse 280px 80px at 170px 420px, rgba(138,106,58,0.95) 0%, rgba(138,106,58,0) 100%),
      /* red and orange foliage on the right */
      radial-gradient(ellipse 170px 170px at 1010px 340px, rgba(201,72,28,0.9) 0%, rgba(201,72,28,0) 70%),
      radial-gradient(ellipse 200px 150px at 1080px 90px, rgba(216,118,31,0.75) 0%, rgba(216,118,31,0) 70%),
      /* golden birches */
      radial-gradient(ellipse 160px 110px at 420px 170px, rgba(210,160,42,0.95) 0%, rgba(210,160,42,0) 100%),
      radial-gradient(ellipse 150px 120px at 640px 160px, rgba(210,160,42,0.9) 0%, rgba(210,160,42,0) 100%),
      radial-gradient(ellipse 90px 90px at 680px 230px, rgba(179,116,28,0.8) 0%, rgba(179,116,28,0) 100%),
      /* pines */
      radial-gradient(ellipse 120px 110px at 500px 240px, rgba(61,77,36,0.95) 0%, rgba(61,77,36,0) 100%),
      linear-gradient(90deg, var(--forest-deep) 0%, var(--forest-dark) 22%, var(--pine-green) 38%, var(--pine-green) 62%, var(--forest-dark) 78%, var(--forest-deep) 100%);
  }
  .brand {
    position: absolute;
    left: 75px;
    top: 90px;
    width: 290px;
    color: var(--text-light);
    text-shadow: 0 2px 8px rgba(0,0,0,0.45);
  }
  .brand__name {
    display: block;
    font-family: "Kaushan Script", cursive;
    font-size: 84px;
    line-height: 0.95;
  }
  .brand__sub {
    display: block;
    margin-top: 18px;
    margin-left: 168px;
    font-family: "Oswald", sans-serif;
    font-size: 18px;
    letter-spacing: 1.5px;
    text-transform: uppercase;
    line-height: 1;
  }
  .tagline {
    position: absolute;
    left: 712px;
    top: 70px;
    width: 460px;
    color: var(--text-light);
    font-family: "Kaushan Script", cursive;
    font-weight: 400;
    text-shadow: 0 2px 8px rgba(0,0,0,0.4);
  }
  .tagline__lead {
    display: block;
    font-size: 64px;
    line-height: 1;
  }
  .tagline__line {
    display: block;
    margin-top: -4px;
    margin-left: 44px;
    white-space: nowrap;
    line-height: 1;
  }
  .tagline__in {
    font-size: 42px;
    margin-right: 8px;
  }
  .tagline__place {
    font-size: 92px;
  }
  .ingredients {
    position: absolute;
    left: 840px;
    top: 252px;
    width: 300px;
    color: var(--text-light);
    font-family: "Kaushan Script", cursive;
    font-size: 25px;
    line-height: 1.3;
    text-align: center;
    text-shadow: 0 2px 8px rgba(0,0,0,0.45);
  }
</style>
</head>
<body>
  <main class="banner">
    <div class="banner__scene" role="img" aria-label="Photograph of a still forest creek in autumn, golden birches and green pines reflected in dark water, rocky banks, red leaves on the right"></div>

    <div class="brand">
      <span class="brand__name">Grey<br>Owl</span>
      <span class="brand__sub">Brewing Co</span>
    </div>

    <h1 class="tagline">
      <span class="tagline__lead">Handcrafted</span>
      <span class="tagline__line"><span class="tagline__in">in</span><span class="tagline__place">Tasmania</span></span>
    </h1>

    <p class="ingredients">Water, hops, malt, yeast<br>and nothing else</p>
  </main>
</body>
</html>
```